Smart Home App Needs 4 Mockup Screens. Extra Work Guaranteed for Winner

BACKGROUND
Our company, Lumora, is launching an exciting new app early next year. And we need some examples of what our app will look like to show to some of the biggest retailers in the world. We hope that this project will lead to regular work as we have a lot of new products planned for the app.

Our app will support baby, home and pet monitors (cameras) as well as the world's first smart pet flap.

The monitors allow you to do much more than just watch live video. By monitoring and providing information on sound, movement and temperature the app provides the user with instant peace of mind wherever they are. If anything has changed the user can be alerted via notifications. If motion is detected the user will receive a clip of the whole event moments after it has happened.

The Smart Pet Flap is packed full of features too. From letting you decide when your pet can or can't go outside from your mobile, to automatically opening if a fire is detected (along with a whole host of other features) - this really is the most advanced pet flap in the world.

REQUIREMENTS
We need 4 mock-up screens creating to show the UI of our app.
1. Camera Home Page
2. Camera Notifications Page
3. Pet Flap Fire Alarm Warning Page
4. Extreme Weather Warning Page

Optional - Happy to Pay the Winner Extra for these Designs
5. Start Up/Log In Page
6. Pet Flap Notification Example
7. Pet Flap Scheduler Page (your choice)
(SEE LUMORA APP DESIGN COMPETITION - ATTACHED)

STYLE GUIDE
As you'll see from our wireframes we want our app to be very minimal and modern. The predominant colour will be white but where colour is used it should be bright (see our colour palette - which we will provide shortly).

INSPIRATION
We love the UI of Finchly (home surveillance). Also check out Vesk (smart thermostat).
(SEE LUMORA UI EXAMPLES ATTACHED)

LOGO
We love our logo. Feel free to use it in creative ways.

So far we're also using it as a kind of beacon to indicate if everything is ok.

LOGO COLOURS & APP COLOURS
As mentioned, we are thinking of using the green logo to indicate that everything is ok (and also for the pet app in general). We reserve red for when something has happened (normally bad) and needs attention, like a fire alarm going off.

The app will be predominantly black and white with the odd minimal flash of colour (probably primary colour)
We'll upload a colour scheme as soon as we have it.

CONTACT
Please message us for more details - we'll do our best to reply promptly.

FUTURE WORK
We will need extra screens made straight after the competition is over and there should be additional regular work after this.

Target Market(s)

Our app will be used by young professionals, to young parents to grandparents. The design must be contemporary but timeless and easy to use no matter how good you are with technology.

Industry/Entity Type

Pet

Font styles to use
Sans Serif

Colors
faee3f
33a6d7
ec1f27
acd036
32b7a4

Requirements
Must have
• Beautiful, minimal design. Make sure you spend time looking at the Finchly and Vesk apps before starting.

For the videos make sure you use sensible images - that you'd expect to see from a monitor (high resolution images if possible)
Nice to have
• Creative use of our logo.
Should not have
• Too much detail/clutter/colours. Ugly fonts.

```html
<!DOCTYPE html>
<html lang="en">
<head>
<meta charset="utf-8">
<title>Lumora – App Screens</title>
<link rel="stylesheet" href="https://fonts.googleapis.com/css2?family=Roboto:wght@100;300;400;500;700&display=swap">
<style>
:root{
  --stage:#e6e6e6;
  --ink:#111111;
  --muted:#555555;
  --rule:#333333;
  --hair:#cfcfcf;
  --paper:#ffffff;
  --paper-soft:#f4f4f4;
  --bar:#0d0d0d;
  --status:#ebebeb;
  --yellow:#faee3f;
  --alert-yellow:#f5e43a;
  --green:#1aa84a;
  --logo:#acd036;
  --sky-top:#4a90d4;
  --sky-bottom:#2a6aa8;
}
*{box-sizing:border-box;margin:0;padding:0}
html,body{width:1200px;height:462px;overflow:hidden}
body{background:var(--stage);font-family:"Roboto",Arial,sans-serif;color:var(--ink);position:relative}

.screen{position:absolute;top:122px;width:124px;height:220px;background:var(--paper);overflow:hidden}
.screen--home{left:112px}
.screen--notifications{left:362px;background:var(--paper-soft)}
.screen--lock{left:612px}
.screen--alarm{left:862px;background:#f7f7f7}

.status-bar{position:absolute;top:0;left:0;right:0;height:8px;background:var(--status);font-size:4px;display:flex;align-items:center;justify-content:space-between;padding:0 3px;color:var(--ink)}
.status-bar--light{background:transparent;color:#fff}
.status-bar .battery{display:inline-block;width:7px;height:3px;border:0.5px solid currentColor;background:currentColor;vertical-align:middle;margin-left:1px}

.nav-bar{position:absolute;top:8px;left:0;right:0;height:12px;background:var(--bar);color:#fff;display:flex;align-items:center;padding:0 3px;font-size:4.5px;font-weight:500}
.nav-bar .menu{width:5px;height:4px;border-top:0.7px solid #fff;border-bottom:0.7px solid #fff;position:relative;margin-right:5px}
.nav-bar .menu::after{content:"";position:absolute;left:0;right:0;top:1.3px;border-top:0.7px solid #fff}
.nav-bar .title{flex:1}
.nav-bar .tab{font-size:3.6px;font-weight:700;padding:1px 3px;margin-left:1px}
.nav-bar .tab--active{background:#fff;color:var(--ink)}
.brand-dot{display:inline-block;width:5px;height:5px;border-radius:50%;background:var(--logo);margin-left:3px}

/* Home */
.feed{position:absolute;top:20px;left:0;right:0;height:88px;background:linear-gradient(135deg,#c9b79a 0%,#e9e3d6 45%,#cfc6b4 75%,#8f7f68 100%)}
.controls{position:absolute;top:110px;left:0;right:0;height:24px;display:flex;justify-content:space-around;align-items:center;padding:0 14px;border-bottom:0.5px solid var(--hair)}
.camera-list{position:absolute;top:135px;left:0;right:0;list-style:none}
.camera-item{height:25px;display:flex;align-items:center;padding:0 10px 0 8px;border-bottom:0.5px solid var(--hair)}
.camera-item .index{font-size:12px;font-weight:500;width:15px}
.camera-item .meta{flex:1;font-size:4.6px;line-height:5.8px}
.camera-item .meta b{font-weight:700;display:block}
.camera-item .signal{width:2.5px;height:2.5px;border-radius:50%;background:var(--yellow)}
.scroll-hint{position:absolute;top:211px;left:0;right:0;text-align:center;font-size:2.6px;color:var(--muted);letter-spacing:.2px}

/* Notifications */
.sheet{position:absolute;top:20px;left:0;right:0;height:66px;background:var(--paper)}
.sheet .rule{position:absolute;left:26px;width:70px;border-top:0.6px solid var(--rule)}
.sheet h1{position:absolute;top:17px;left:26px;font-size:7px;font-weight:300;line-height:8.5px}
.sheet .change{position:absolute;top:41px;left:26px;font-size:3.6px;font-weight:700;letter-spacing:.1px}
.event-list{position:absolute;top:87px;left:0;right:0;list-style:none;background:var(--paper)}
.event{height:21px;display:flex;align-items:center;padding:0 8px 0 6px;border-bottom:0.5px solid var(--hair)}
.event .icon{width:14px;display:flex;justify-content:center}
.event .text{width:70px;font-size:3.8px;line-height:4.6px;padding-left:6px}
.event .text b{display:block;font-weight:700}
.event .view{margin-left:auto;display:flex;flex-direction:column;align-items:center;font-size:2.6px;font-weight:700}

/* Lock */
.lock-scene{position:absolute;inset:0;background:linear-gradient(180deg,var(--sky-top) 0%,var(--sky-bottom) 100%)}
.clock{position:absolute;top:17px;left:0;right:0;text-align:center;color:#fff;font-weight:100;font-size:20px;letter-spacing:.5px}
.date{position:absolute;top:41px;left:0;right:0;text-align:center;color:#fff;font-size:4px;font-weight:300}
.notice{position:absolute;top:83px;left:18px;width:88px;height:56px;background:rgba(40,40,40,.82);color:#fff;text-align:center}
.notice .app{margin-top:14px;font-size:4.6px;font-weight:700;letter-spacing:.3px;display:flex;align-items:center;justify-content:center;gap:3px}
.notice .app .brand-dot{margin:0;width:4px;height:4px}
.notice p{margin-top:14px;font-size:3.8px;font-weight:300}

/* Alarm */
.warning{position:absolute;top:22px;left:24px}
.alarm-rule{position:absolute;left:26px;width:72px;border-top:0.6px solid var(--rule)}
.alarm-title{position:absolute;top:101px;left:26px;font-size:6.4px;font-weight:300}
.alarm-body{position:absolute;top:115px;left:26px;width:72px;font-size:3.6px;line-height:4.6px}
.options{position:absolute;top:147px;left:26px;width:72px;list-style:none;border-top:0.6px solid var(--rule)}
.options li{min-height:11px;padding:1.5px 0;display:flex;align-items:center;font-size:3.6px;line-height:4.6px;border-bottom:0.6px solid var(--rule)}
.options li:last-child{border-bottom:none}
.alarm-mark{position:absolute;top:197px;left:88px;margin:0}
</style>
</head>
<body>

<section class="screen screen--home">
  <div class="status-bar"><span>●●●○○ VOLT</span><span>4:21 PM</span><span>100% <i class="battery"></i></span></div>
  <header class="nav-bar"><span class="menu"></span><span class="title">Cameras</span><span class="tab tab--active">NOW</span><span class="tab">EARLIER</span><span class="brand-dot"></span></header>
  <div class="feed" role="img" aria-label="Live video of a baby sleeping in a cot"></div>
  <div class="controls">
    <svg width="9" height="12" viewBox="0 0 9 12"><rect x="2.5" y="0.5" width="4" height="7" rx="2" fill="#222"/><path d="M1 5.5a3.5 3.5 0 0 0 7 0M4.5 9v2.5M2.5 11.5h4" stroke="#222" fill="none" stroke-width="0.8"/></svg>
    <svg width="6" height="12" viewBox="0 0 6 12"><rect x="2" y="0.5" width="2" height="8" rx="1" fill="none" stroke="#222" stroke-width="0.8"/><circle cx="3" cy="9.5" r="2.2" fill="#222"/></svg>
    <svg width="10" height="10" viewBox="0 0 10 10"><rect x="0" y="5" width="2.5" height="5" fill="#222"/><rect x="3.6" y="2" width="2.5" height="8" fill="#222"/><rect x="7.2" y="0" width="2.5" height="10" fill="#222"/></svg>
    <svg width="12" height="12" viewBox="0 0 12 12" fill="#222"><rect x="5.4" y="2" width="1.2" height="8"/><rect x="2" y="5.4" width="8" height="1.2"/><path d="M6 0l2 2.3H4zM6 12l2-2.3H4zM0 6l2.3-2v4zM12 6l-2.3-2v4z"/></svg>
  </div>
  <ul class="camera-list">
    <li class="camera-item"><span class="index">1</span><span class="meta"><b>Nursery Camera</b>Currently Viewing</span><span class="signal"></span></li>
    <li class="camera-item"><span class="index">2</span><span class="meta"><b>Patio Camera</b>Last checked: 7:52pm</span><span class="signal"></span></li>
    <li class="camera-item"><span class="index">3</span><span class="meta"><b>Kitchen Camera</b>Last checked: 3:16pm</span><span class="signal"></span></li>
  </ul>
  <p class="scroll-hint">— SCROLL FOR MORE</p>
</section>

<section class="screen screen--notifications">
  <div class="status-bar"><span>●●●○○ VOLT</span><span>4:21 PM</span><span>100% <i class="battery"></i></span></div>
  <header class="nav-bar"><span class="menu"></span><span class="title">Cameras</span><span class="tab">NOW</span><span class="tab tab--active">EARLIER</span><span class="brand-dot"></span></header>
  <div class="sheet">
    <span class="rule" style="top:15px"></span>
    <h1>Nursery Camera<br>Notifications</h1>
    <span class="rule" style="top:37px"></span>
    <span class="change">CHANGE CAMERA</span>
    <span class="rule" style="top:48px"></span>
  </div>
  <ul class="event-list">
    <li class="event"><span class="icon"><svg width="11" height="8" viewBox="0 0 11 8" fill="none" stroke="#222" stroke-width="0.7"><circle cx="5.5" cy="4" r="1" fill="#222"/><path d="M3.5 2a3 3 0 0 0 0 4M7.5 2a3 3 0 0 1 0 4M2 0.8a5 5 0 0 0 0 6.4M9 0.8a5 5 0 0 1 0 6.4"/></svg></span><span class="text"><b>7:15am</b>There's a lot of movement and noise.</span><span class="view"><svg width="7" height="7" viewBox="0 0 7 7"><circle cx="3.5" cy="3.5" r="3.5" fill="#111"/><path d="M2.7 2v3l2.3-1.5z" fill="#fff"/></svg>VIEW</span></li>
    <li class="event"><span class="icon"><svg width="8" height="8"><circle cx="4" cy="4" r="4" fill="var(--green)"/></svg></span><span class="text"><b>6:07am</b>All is calm.</span><span class="view"><svg width="7" height="7" viewBox="0 0 7 7"><circle cx="3.5" cy="3.5" r="3.5" fill="#111"/><path d="M2.7 2v3l2.3-1.5z" fill="#fff"/></svg>VIEW</span></li>
    <li class="event"><span class="icon"><svg width="5" height="10" viewBox="0 0 5 10"><rect x="1.5" y="0" width="2" height="6" rx="1" fill="#222"/><path d="M0.5 4.5a2 2 0 0 0 4 0M2.5 6.5v3" stroke="#222" fill="none" stroke-width="0.6"/></svg></span><span class="text"><b>5:32am</b>There's some loud noise.</span><span class="view"><svg width="7" height="7" viewBox="0 0 7 7"><circle cx="3.5" cy="3.5" r="3.5" fill="#111"/><path d="M2.7 2v3l2.3-1.5z" fill="#fff"/></svg>VIEW</span></li>
    <li class="event"><span class="icon"><svg width="4" height="10" viewBox="0 0 4 10"><rect x="1.2" y="0.3" width="1.6" height="6.5" rx="0.8" fill="none" stroke="#222" stroke-width="0.6"/><circle cx="2" cy="8" r="1.7" fill="#222"/></svg></span><span class="text"><b>4:48am</b>The room temperature has just dropped to 18 degrees.</span><span class="view"><svg width="7" height="7" viewBox="0 0 7 7"><circle cx="3.5" cy="3.5" r="3.5" fill="#111"/><path d="M2.7 2v3l2.3-1.5z" fill="#fff"/></svg>VIEW</span></li>
    <li class="event"><span class="icon"><svg width="11" height="8" viewBox="0 0 11 8" fill="none" stroke="#222" stroke-width="0.7"><circle cx="5.5" cy="4" r="1" fill="#222"/><path d="M3.5 2a3 3 0 0 0 0 4M7.5 2a3 3 0 0 1 0 4M2 0.8a5 5 0 0 0 0 6.4M9 0.8a5 5 0 0 1 0 6.4"/></svg></span><span class="text"><b>4:11am</b>There's a lot of movement.</span><span class="view"><svg width="7" height="7" viewBox="0 0 7 7"><circle cx="3.5" cy="3.5" r="3.5" fill="#111"/><path d="M2.7 2v3l2.3-1.5z" fill="#fff"/></svg>VIEW</span></li>
  </ul>
</section>

<section class="screen screen--lock">
  <div class="lock-scene" role="img" aria-label="Lock screen wallpaper photograph"></div>
  <div class="status-bar status-bar--light"><span>●●●○○ VOLT</span><span>4:21 PM</span><span>100% <i class="battery"></i></span></div>
  <p class="clock">04:42</p>
  <p class="date">Wednesday, 23 October</p>
  <div class="notice">
    <div class="app"><span class="brand-dot"></span>LUMORA</div>
    <p>Tigger has just got home!</p>
  </div>
</section>

<section class="screen screen--alarm">
  <div class="status-bar"><span>●●●○○ VOLT</span><span>4:21 PM</span><span>100% <i class="battery"></i></span></div>
  <svg class="warning" width="76" height="68" viewBox="0 0 76 68"><path d="M38 2 L74 66 H2 Z" fill="var(--alert-yellow)" stroke="var(--alert-yellow)" stroke-width="4" stroke-linejoin="round"/><path d="M34.5 22h7l-1.5 24h-4z" fill="#fff"/><circle cx="38" cy="54" r="3.8" fill="#fff"/></svg>
  <span class="alarm-rule" style="top:98px"></span>
  <h1 class="alarm-title">Fire Alarm</h1>
  <span class="alarm-rule" style="top:111px"></span>
  <p class="alarm-body">Your fire alarm is going off. Rex is already outside so we've locked him out as a precaution. What do you want to do?</p>
  <ul class="options">
    <li>Keep him locked out until further notice.</li>
    <li>False alarm. Let him back in.</li>
    <li>Make a call.</li>
  </ul>
  <span class="brand-dot alarm-mark"></span>
</section>

</body>
</html>
```